Web Design Project

We need a design for the actual web.
http://mirela.vunto.example/
It will be a cakes and cupcakes online shop.

It is a one page site, with five anchors.

Inicio (Home)
Here it will show a brief explanation about our shop, just explaining we sell really nice cakes and cupcakes. Also we want to show a slide gallery, like the one it is working, but with not nice choosen pictures.

Productos/Tortas
This two anchors will be just one at the end, but I wanted to show the two options for accessing the different products, tabs or buttons. You can click on the firsts images on that links for see the "pop up image" with a better explanation of every product.

Contacto
Here it will show a little form, that will only appear in smartphones and maybe tablets, this form needs to be similar and much more simple than the principal form (the next anchor), so just focus on it once the next one its done.

Form
This will be the way the users will send the orders, its a complex form, focused on the UX. We dont want the user to type too much and we want it to surprise the user and fell really comfortable.

Industry/Entity Type

Tv

Requirements
Must have

• -Must have side menu, but you can redesign it completelly, but with the same structure
-Its important to focus all the content in the top and middle, we arent sure about users screens and it we set info at the footer, maybe its not gonna show (no scroll vertical).
-You can change all the colours of the site, we are open to new visions, you can surprise us.

```html
<!DOCTYPE html>
<html lang="es">
<head>
<meta charset="utf-8">
<title>Rosa Dulce – Handmade Bakery</title>
<link href="https://fonts.googleapis.com/css2?family=Oswald:wght@300&family=Alegreya:ital,wght@1,400;1,500&family=Comfortaa:wght@300&family=Open+Sans&display=swap" rel="stylesheet">
<style>
  :root{
    --page:#f4f4f4;
    --shell:#e9e9e9;
    --shell-edge:#dcdcdc;
    --panel:#ffffff;
    --brand:#444444;
    --tagline:#8a8a8a;
    --headline:#8b2a35;
    --menu-text:#444444;
    --menu-line:#cfcfcf;
    --active:#ef5a5f;
    --arrow:#6a6a6a;
    --dot:#dedede;
    --dot-active:#ef5a7a;
    --caption-bg:rgba(60,55,50,.55);
  }
  *{box-sizing:border-box;margin:0;padding:0}
  html,body{width:1200px;height:816px;overflow:hidden}
  body{
    position:relative;
    background:repeating-linear-gradient(135deg,#f6f6f6 0 3px,#efefef 3px 4px);
    font-family:"Open Sans",sans-serif;
  }
  .shell{
    position:absolute;left:72px;top:24px;width:1054px;height:696px;
    background:repeating-linear-gradient(135deg,#ededed 0 3px,#e6e6e6 3px 4px);
    border-radius:10px;border:1px solid var(--shell-edge);
  }
  .shell-shadow{
    position:absolute;left:130px;top:716px;width:940px;height:30px;
    background:radial-gradient(ellipse at center top,rgba(0,0,0,.22),rgba(0,0,0,0) 70%);
  }
  .brand-mark{
    position:absolute;left:125px;top:36px;width:64px;height:64px;border-radius:50%;
    background:#f8f8f8;border:1px solid #d6d6d6;
  }
  .brand-name{
    position:absolute;left:228px;top:28px;font-family:"Oswald",sans-serif;
    font-weight:300;font-size:32px;line-height:40px;color:var(--brand);letter-spacing:1px;
  }
  .brand-tagline{
    position:absolute;left:510px;top:36px;font-family:"Oswald",sans-serif;
    font-weight:300;font-size:20px;line-height:28px;color:var(--tagline);letter-spacing:1px;
  }
  .social{position:absolute;top:32px;left:928px;display:flex;gap:12px}
  .social span{
    width:36px;height:36px;border-radius:50%;
    background:radial-gradient(circle at 40% 35%,#f2f2f2,#c9c9c9);
    border:1px solid #b5b5b5;display:flex;align-items:center;justify-content:center;
  }
  .content{
    position:absolute;left:232px;top:79px;width:874px;height:617px;
    background:var(--panel);border-radius:10px;
    box-shadow:0 1px 3px rgba(0,0,0,.12);
  }
  .headline{
    position:absolute;left:0;right:0;top:20px;text-align:center;
    font-family:"Alegreya",serif;font-style:italic;font-weight:400;font-size:34px;color:var(--headline);
    text-shadow:1px 2px 2px rgba(0,0,0,.18);
  }
  .menu{position:absolute;left:84px;top:116px;width:148px;list-style:none}
  .menu li{
    height:108px;display:flex;align-items:center;justify-content:center;
    font-family:"Oswald",sans-serif;font-weight:300;font-size:26px;color:var(--menu-text);
    border-bottom:1px solid var(--menu-line);margin-right:12px;
  }
  .menu li.active{
    margin-right:0;background:var(--panel);border-bottom:none;
    border-left:19px solid var(--active);border-radius:6px 0 0 6px;padding-right:12px;
    box-shadow:-1px 1px 3px rgba(0,0,0,.12);
  }
  .slider-frame{
    position:absolute;left:258px;top:172px;width:822px;height:472px;
    border:2px solid #e6e6e6;border-radius:8px;background:#f7f7f7;
  }
  .slide{
    position:absolute;left:295px;top:174px;width:750px;height:466px;overflow:hidden;
    background:
      radial-gradient(ellipse 48% 42% at 48% 55%,#f3ead2 0,#e9dbb8 55%,rgba(233,219,184,0) 100%),
      radial-gradient(ellipse 30% 30% at 85% 40%,#d9402e,rgba(217,64,46,0) 100%),
      linear-gradient(160deg,#6e2a1e 0%,#a55a2a 35%,#c9a46a 60%,#7a3a22 100%);
  }
  .slide-title{
    position:absolute;right:20px;top:6px;text-align:right;
    font-family:"Comfortaa",sans-serif;font-weight:300;font-size:42px;line-height:51px;
    color:#fff;letter-spacing:1px;
  }
  .slide-play{position:absolute;left:1052px;top:182px}
  .caption{
    position:absolute;left:0;bottom:0;width:100%;height:206px;background:var(--caption-bg);
    text-align:center;color:#fff;font-family:"Alegreya",serif;font-style:italic;
    text-shadow:1px 1px 2px rgba(0,0,0,.5);
  }
  .caption h2{font-weight:500;font-size:24px;margin-top:8px}
  .caption p{font-size:18px;line-height:19px;margin-top:16px;padding:0 26px}
  .caption .hide{
    position:absolute;right:6px;top:6px;font-family:"Open Sans",sans-serif;font-style:normal;
    font-size:10px;display:flex;align-items:center;gap:4px;text-shadow:none;
  }
  .arrow{
    position:absolute;top:371px;width:50px;height:72px;background:var(--arrow);
    display:flex;align-items:center;justify-content:center;
  }
  .arrow.prev{left:239px}
  .arrow.next{left:1048px}
  .dots{position:absolute;left:581px;top:661px;display:flex;gap:22px}
  .dots span{width:14px;height:14px;border-radius:50%;background:var(--dot);box-shadow:inset 0 1px 2px rgba(0,0,0,.2)}
  .dots span.current{background:var(--dot-active);box-shadow:0 0 0 3px #f7c3cf}
</style>
</head>
<body>
  <div class="shell-shadow"></div>
  <div class="shell"></div>

  <div class="brand-mark"></div>
  <div class="brand-name">Rosa Dulce</div>
  <div class="brand-tagline">Handmade Bakery</div>

  <div class="social">
    <span aria-label="Email">
      <svg width="20" height="14" viewBox="0 0 20 14"><rect x="1" y="1" width="18" height="12" rx="1.5" fill="#fff" stroke="#8a8a8a"/><path d="M1 1l9 7 9-7" fill="none" stroke="#8a8a8a"/></svg>
    </span>
    <span aria-label="Red social"></span>
    <span aria-label="Red social"></span>
    <span aria-label="Red social"></span>
  </div>

  <div class="content">
    <h1 class="headline">Los mejores Cupcakes y Pasteles de Santiago</h1>
  </div>

  <ul class="menu">
    <li class="active">INICIO</li>
    <li>PRODUCTOS</li>
    <li>TORTAS</li>
    <li>CONTACTO</li>
    <li>FORM</li>
  </ul>

  <div class="slider-frame"></div>
  <div class="slide" role="img" aria-label="Foto de una torta de chocolate blanco con frambuesas sobre un plato con blonda">
    <div class="slide-title">torta chocolate<br>blanco frambuesa</div>
    <div class="caption">
      <div class="hide">Hide
        <svg width="16" height="16" viewBox="0 0 16 16"><circle cx="8" cy="8" r="7" fill="none" stroke="#fff"/><path d="M4.5 6.5L8 10l3.5-3.5" fill="#fff"/></svg>
      </div>
      <h2>"tip-bottom"</h2>
      <p>Finalmente ya está disponible en Santiago de Chile nuestro catálogo de sabrosos Cupcakes y Tortas</p>
      <p>Con ingredientes 100% naturales y elaborados artesanalmente</p>
      <p>No solo hay que tener en cuenta la presentación fabulosa de los mismos, lo que más destacan nuestros clientes es el sabor exquisito y la textura</p>
    </div>
  </div>
  <svg class="slide-play" width="20" height="20" viewBox="0 0 20 20"><circle cx="10" cy="10" r="8" fill="#eee" stroke="#777"/><path d="M8 6l6 4-6 4z" fill="#777"/></svg>

  <div class="arrow prev"><svg width="22" height="40" viewBox="0 0 22 40"><path d="M19 3L4 20l15 17" fill="none" stroke="#fff" stroke-width="3"/></svg></div>
  <div class="arrow next"><svg width="22" height="40" viewBox="0 0 22 40"><path d="M3 3l15 17L3 37" fill="none" stroke="#fff" stroke-width="3"/></svg></div>

  <div class="dots">
    <span></span><span class="current"></span><span></span><span></span><span></span><span></span>
  </div>
</body>
</html>
```